I need a website for my moving company Brisk Haulers LLC. I would like the following text included in my website. I have purchased the domain briskhaulersco.example from nametrellis.example. I am not familiar with SEO or other techniques that help my page on search engines but would like the website to be optimized for Scoutly search engine. I have attached our logo below and would like it to be used in the design. The colors in the logo can be used also in the design.
Home/About Us
At Brisk Haulers LLC, we know moving. It can be difficult, stressful, and a real pain in the backside. But it doesn’t have to be! When you partner with Brisk, you get the benefits of a professional moving team that is licensed and insured for your protection along with years of experience and a dedication to providing the highest quality service, each and every time.
Our Services
We do a wide variety of local moves, including apartments, single-family homes, retirement communities, dorms, condos, and many more! Our movers are trained to protect your belongings and your home – all pieces of furniture are padded and stretch wrapped free of charge, ensuring your items and home are damage-free at the end of your move. Having added stress about packing up your home prior to moving? We’ve got you covered with our full service packing and unpacking services, too.
What You Get
When you partner with BRISK, you’ll get the best service in the industry, as well as:
* The Use of Packing & Moving Materials: The hourly rate includes the use of our dollies, ratchet straps, pads, moving tools, and property protection like floor mats, door-jamb protectors, stairwell protectors, and plenty of muscle!
• Trained, Licensed, and Insured Movers: All of our movers are highly trained to provide you with the best service, and to ensure the protection of you and your items.
• Professional: Honest, Uniformed, Nice, Knowledgeable Service is what you’ll get with every member of our moving teams.
• Custom Service for Every Move: Every move is as unique as the person or business moving. Our training and equipment allows us to customize every project to ensure the very best for every client.
Target Market(s)
Home and Business movers
Industry/Entity Type
Moving Company
Colors
Designer to choose colors to be used in the design.
Requirements
Must have
- 2 sides
Nice to have
- Colorful design with logo included.
Should not have
- animated characters

```html
<!DOCTYPE html>
<html lang="en">
<head>
<meta charset="utf-8">
<title>Brisk Haulers LLC – Larkfield, ST</title>
<link href="https://fonts.googleapis.com/css2?family=Bree+Serif&family=Fira+Sans+Condensed:wght@500;600;700&family=Open+Sans:wght@400;600;700&display=swap" rel="stylesheet">
<style>
:root{
  --orange:#f7941d;
  --orange-dark:#ee7f1a;
  --green:#6cb52d;
  --green-dark:#4f9a1f;
  --ink:#333333;
  --muted:#555555;
  --charcoal:#2b2b2b;
  --footer:#1f1f1f;
  --white:#ffffff;
}
*{box-sizing:border-box;margin:0;padding:0}
html,body{width:1200px;height:3141px;overflow:hidden}
body{font-family:"Open Sans",Arial,sans-serif;color:var(--ink);background:var(--white);position:relative}
.abs{position:absolute}

/* Hero */
.hero{left:0;top:0;width:1200px;height:698px;background:linear-gradient(120deg,#3d4a55 0%,#6e7f8c 35%,#b8a98e 60%,#4a5b6a 100%);overflow:hidden}
.hero-shade{left:0;top:0;width:1200px;height:150px;background:linear-gradient(#000a,#0000)}
.brand{left:70px;top:34px;display:flex;align-items:center;gap:10px;font-family:"Fira Sans Condensed",sans-serif;font-weight:700;font-size:22px;color:var(--orange)}
.brand-dot{width:26px;height:26px;border-radius:50%;background:var(--orange)}
.nav{right:60px;top:44px;display:flex;align-items:center;gap:40px;font-family:"Open Sans",sans-serif;font-weight:600;font-size:16px;color:var(--white)}
.nav .call{display:flex;align-items:center;gap:8px;font-size:18px}
.nav .call b{font-size:20px}
.hero-badge{left:121px;top:121px;width:448px;height:448px;border-radius:50%;background:linear-gradient(120deg,var(--orange) 15%,var(--green) 85%);text-align:center;color:var(--white)}
.hero-badge .brand-mini{margin-top:118px;font-family:"Fira Sans Condensed",sans-serif;font-weight:700;font-size:18px}
.hero-badge h1{font-family:"Bree Serif",serif;font-weight:400;font-size:42px;line-height:1.2;margin-top:18px}
.btn{display:inline-block;font-family:"Open Sans",sans-serif;font-weight:600;color:var(--white);background:var(--orange);border:3px solid var(--white);border-radius:24px;text-transform:uppercase}
.hero-badge .btn{margin-top:24px;font-size:14px;padding:10px 26px}
.hero-badge .phone{margin-top:24px;font-size:22px;font-weight:600}

/* About / services */
.card-photo{top:758px;height:335px;border:4px solid #333;background:linear-gradient(135deg,#b9cfe0,#d9c4a2 60%,#8aa0b5)}
.card-photo.services{background:linear-gradient(135deg,#dfe9f2,#e8d4bc 55%,#a9b9c7)}
.card-title{top:1057px;height:74px;width:472px;background:var(--white);padding:18px 24px}
.card-title h2{font-family:"Fira Sans Condensed",sans-serif;font-weight:700;font-size:36px;color:var(--green-dark);line-height:1}
.card-title .rule{position:absolute;left:24px;right:24px;bottom:6px;height:1px;background:#ddd}
.card-text{top:1150px;width:445px;font-size:14px;line-height:26px;color:var(--muted)}

/* Guarantee */
.guarantee{left:0;top:1436px;width:1200px;height:694px;background:linear-gradient(120deg,#d9dcdc,#f2f2f0 50%,#c7ccd0);overflow:hidden}
.guarantee-photo{left:560px;top:0;width:640px;height:694px;background:linear-gradient(90deg,#7a8ea4 0%,#c9c4bb 40%,#3d5a8a 70%,#e2e2e2 100%)}
.guarantee-panel{left:0;top:0;width:653px;height:694px;background:linear-gradient(90deg,var(--green) 0%,#73b92f 70%,rgba(108,181,45,.85) 100%);color:var(--white);padding:40px 75px}
.guarantee-panel h2{font-family:"Fira Sans Condensed",sans-serif;font-weight:700;font-size:36px}
.guarantee-panel .intro{font-size:14px;line-height:24px;margin-top:20px;width:420px}
.feature-grid{display:grid;grid-template-columns:265px 220px;margin-top:24px}
.feature{padding:0 20px 28px 0;min-height:265px}
.feature:nth-child(2n){padding-left:20px;border-left:1px solid rgba(255,255,255,.4)}
.feature:nth-child(n+3){min-height:auto;padding-top:6px}
.feature h3{font-family:"Open Sans",sans-serif;font-weight:700;font-size:15px;line-height:22px;margin-bottom:14px}
.feature p{font-size:13px;line-height:26px}

/* Subscribe / booking */
.subscribe{left:75px;top:2184px;width:513px;height:416px;background:var(--charcoal);text-align:center;color:var(--white);padding-top:24px}
.icon-ring{width:100px;height:100px;border-radius:50%;background:linear-gradient(135deg,var(--orange),var(--green));margin:0 auto;display:flex;align-items:center;justify-content:center}
.subscribe h2{font-family:"Fira Sans Condensed",sans-serif;font-weight:700;font-size:36px;color:var(--green);margin-top:16px}
.subscribe p{font-size:16px;line-height:26px;margin-top:8px}
.email-field{margin:24px auto 0;width:457px;height:48px;background:var(--white);color:#777;text-align:left;padding:15px 16px;font-size:12px}
.signup{margin:22px auto 0;width:457px;height:50px;background:var(--orange);font-weight:600;font-size:18px;line-height:50px;text-transform:uppercase}
.booking{left:614px;top:2184px;width:511px;height:416px;background:linear-gradient(135deg,#2e4c7a,#6c7d8e 50%,#2b3e5e);text-align:center;color:var(--white)}
.booking h2{font-family:"Bree Serif",serif;font-weight:400;font-size:36px;line-height:36px;margin-top:42px;text-transform:uppercase}
.booking-box{margin:12px auto 0;width:270px;height:150px;background:rgba(30,30,30,.85);padding-top:10px}
.booking-box h3{font-weight:600;font-size:22px}
.booking-stats{display:flex;justify-content:center;gap:70px;margin-top:10px;font-size:16px}
.booking-stats div{display:flex;flex-direction:column;align-items:center;gap:8px}
.coin{width:50px;height:50px;border-radius:50%;display:flex;align-items:center;justify-content:center}
.booking .btn{margin-top:14px;font-size:14px;padding:8px 24px}

/* Contact */
.contact{left:0;top:2655px;width:496px;height:423px;background:linear-gradient(120deg,var(--orange) 0%,#c3a528 45%,var(--green) 100%);color:var(--white);padding:34px 0 0 100px}
.contact h2{font-family:"Fira Sans Condensed",sans-serif;font-weight:700;font-size:36px}
.contact-item{display:flex;gap:14px;margin-top:22px}
.contact-item svg{flex:none;margin-top:2px}
.contact-item h3{font-weight:600;font-size:17px}
.contact-item p{font-size:12px;line-height:20px;margin-top:2px}
.map{left:496px;top:2655px;width:704px;height:423px;background:linear-gradient(135deg,#e8e6e1,#dcdad3 60%,#cfd9c4)}
.map-directions{left:44px;top:10px;background:var(--green);color:var(--white);font-size:12px;font-weight:600;padding:8px 16px;text-transform:uppercase}
.footer{left:0;top:3078px;width:1200px;height:63px;background:var(--footer);color:var(--white);font-size:13px;padding:0 70px;display:flex;align-items:center;justify-content:space-between}
.social-dot{width:28px;height:28px;border-radius:50%;background:var(--white)}
</style>
</head>
<body>

<section class="hero abs" role="img" aria-label="Photo of two movers unloading boxes from a moving van">
  <div class="hero-shade abs"></div>
</section>
<div class="brand abs"><span class="brand-dot"></span>BRISK HAULERS</div>
<nav class="nav abs">
  <span>HOME</span><span>ABOUT US</span><span>SERVICES</span><span>FAQ</span><span>CONTACT US</span>
  <span class="call"><svg width="18" height="18" viewBox="0 0 24 24"><path d="M6.6 10.8a15 15 0 006.6 6.6l2.2-2.2a1 1 0 011-.25 11.4 11.4 0 003.6.6 1 1 0 011 1V20a1 1 0 01-1 1A17 17 0 013 4a1 1 0 011-1h3.5a1 1 0 011 1c0 1.25.2 2.45.6 3.6a1 1 0 01-.25 1z" fill="none" stroke="#fff" stroke-width="1.8"/></svg>Call Us: <b>(555) 014-2290</b></span>
</nav>
<div class="hero-badge abs">
  <div class="brand-mini">BRISK HAULERS</div>
  <h1>Brisk Haulers LLC<br>Larkfield, ST</h1>
  <span class="btn">Book Today</span>
  <div class="phone">(555) 014-2290</div>
</div>

<div class="card-photo abs" style="left:75px;width:515px" role="img" aria-label="Photo of two smiling movers carrying boxes beside a van"></div>
<div class="card-title abs" style="left:94px"><h2>ABOUT US</h2><span class="rule"></span></div>
<p class="card-text abs" style="left:116px">At Brisk Haulers LLC, we know moving. It can be difficult, stressful, and a real pain in the backside. But it doesn’t have to be! When you partner with Brisk, you get the benefits of a professional moving team that is licensed and insured for your protection along with years of experience and a dedication to providing the highest quality service, each and every time.</p>

<div class="card-photo services abs" style="left:614px;width:511px" role="img" aria-label="Photo of a family unpacking moving boxes at home"></div>
<div class="card-title abs" style="left:633px"><h2>OUR SERVICES</h2><span class="rule"></span></div>
<p class="card-text abs" style="left:655px">We do a wide variety of local moves, including apartments, single-family homes, retirement communities, dorms, condos, and many more! Our movers are trained to protect your belongings and your home – all pieces of furniture are padded and stretch wrapped free of charge, ensuring your items and home are damage-free at the end of your move. Having added stress about packing up your home prior to moving? We’ve got you covered with our full service packing and unpacking services, too.</p>

<section class="guarantee abs">
  <div class="guarantee-photo abs" role="img" aria-label="Photo of two uniformed movers standing in front of a white van"></div>
  <div class="guarantee-panel abs">
    <h2>OUR GAURANTEE</h2>
    <p class="intro">When you partner with BRISK, you’ll get the best service in the industry, as well as:</p>
    <div class="feature-grid">
      <div class="feature"><h3>The Use of Packing &amp;<br>Moving Materials:</h3><p>The hourly rate includes the use of our dollies, ratchet straps, pads, moving tools, and property protection like floor mats, door-jamb protectors, stairwell protectors, and plenty of muscle!</p></div>
      <div class="feature"><h3>Trained, Licensed, and Insured Movers:</h3><p>All of our movers are highly trained to provide you with the best service, and to ensure the protection of you and your items.</p></div>
      <div class="feature"><h3>Professional:</h3><p>Honest, Uniformed, Nice, Knowledgeable Service is what you’ll get with every member of our moving teams.</p></div>
      <div class="feature"><h3>Custom Service for Every Move:</h3><p>Every move is as unique as the person or business moving. Our training and equipment allows us to customize every project to ensure the very best for every client.</p></div>
    </div>
  </div>
</section>

<section class="subscribe abs">
  <div class="icon-ring"><svg width="50" height="36" viewBox="0 0 50 36"><rect x="2" y="2" width="46" height="32" fill="none" stroke="#fff" stroke-width="2.5"/><path d="M2 2l23 18L48 2" fill="none" stroke="#fff" stroke-width="2.5"/></svg></div>
  <h2>SUBSCRIBE</h2>
  <p>Sign up to hear from us<br>about specials, packing tips, and more.</p>
  <div class="email-field">Email Address</div>
  <div class="signup">Sign Up</div>
</section>

<section class="booking abs" role="img" aria-label="Photo of movers carrying boxes, behind the booking panel">
  <h2>Book an<br>Appointment</h2>
  <div class="booking-box">
    <h3>Moving Service</h3>
    <div class="booking-stats">
      <div><span class="coin" style="background:var(--green)"><svg width="20" height="26" viewBox="0 0 20 26"><path d="M2 2h16M2 24h16M4 2c0 8 12 8 12 11S4 16 4 24M16 2c0 8-12 8-12 11s12 3 12 11" fill="none" stroke="#fff" stroke-width="2"/></svg></span>1 hour</div>
      <div><span class="coin" style="background:var(--orange)"><svg width="24" height="24" viewBox="0 0 24 24"><circle cx="12" cy="12" r="10" fill="none" stroke="#fff" stroke-width="2"/><text x="12" y="17" text-anchor="middle" font-family="Open Sans,sans-serif" font-size="14" font-weight="700" fill="#fff">$</text></svg></span>$125.00</div>
    </div>
  </div>
  <span class="btn">Book Today</span>
</section>

<section class="contact abs">
  <h2>CONTACT US</h2>
  <div class="contact-item">
    <svg width="24" height="24" viewBox="0 0 24 24"><rect x="2" y="4" width="20" height="18" rx="2" fill="none" stroke="#fff" stroke-width="2"/><path d="M2 9h20M7 2v4M17 2v4" stroke="#fff" stroke-width="2"/></svg>
    <div><h3>Schedule Your Move</h3><p>To arrange movers, please contact us at your<br>convenience. We look forward to meeting you soon.</p></div>
  </div>
  <div class="contact-item">
    <svg width="24" height="24" viewBox="0 0 24 24"><path d="M12 22s7-7.5 7-12.5a7 7 0 00-14 0C5 14.5 12 22 12 22z" fill="none" stroke="#fff" stroke-width="2"/><circle cx="12" cy="9.5" r="2.5" fill="#fff"/></svg>
    <div><h3>Brisk Haulers LLC</h3><p>742 Linden St., Larkfield, ST 00421</p></div>
  </div>
  <div class="contact-item">
    <svg width="24" height="24" viewBox="0 0 24 24"><path d="M6.6 10.8a15 15 0 006.6 6.6l2.2-2.2a1 1 0 011-.25 11.4 11.4 0 003.6.6 1 1 0 011 1V20a1 1 0 01-1 1A17 17 0 013 4a1 1 0 011-1h3.5a1 1 0 011 1c0 1.25.2 2.45.6 3.6a1 1 0 01-.25 1z" fill="none" stroke="#fff" stroke-width="2"/></svg>
    <div><h3>(555) 014-2290</h3></div>
  </div>
  <div class="contact-item">
    <svg width="24" height="24" viewBox="0 0 24 24"><circle cx="12" cy="12" r="10" fill="none" stroke="#fff" stroke-width="2"/><path d="M2 12h20M12 2c3 3 3 17 0 20M12 2c-3 3-3 17 0 20" fill="none" stroke="#fff" stroke-width="1.5"/></svg>
    <div><h3>Service Area</h3><p>Greater Larkfield</p></div>
  </div>
</section>

<section class="map abs" role="img" aria-label="Street map showing the office location">
  <div class="map-directions abs">Get Directions</div>
</section>

<footer class="footer abs">
  <span>Copyright © 2017 Brisk Haulers LLC - All Rights Reserved.</span>
  <span class="social-dot"></span>
</footer>

</body>
</html>
```